Criação de Papelaria (6 itens) para Arquitetura
" Sou recém formada em Design de Interiores e pretendo começar a divulgar meu negócio. Já fiz alguns trabalhos / projetos, mas ainda não consegui alavancar minha marca. Meu foco será a realização de projetos residenciais, comerciais e empresariais. As atividades vão desde a entrevista inicial para entendimento das necessidades do cliente, passando pela preparação dos projetos com imagens renderizadas, plantas baixas, projetos de marcenaria, iluminação, gesso etc., incluindo também acompanhamento a lojas para escolha de materiais / móveis até o acompanhamento da obra e fiscalização dos trabalhos executados por terceiros. "

```html
<!DOCTYPE html>
<html lang="pt-BR">
<head>
<meta charset="UTF-8">
<title>Lia Moraes – Bloco de Notas</title>
<link href="https://fonts.googleapis.com/css2?family=Montserrat:wght@300;400;500&display=swap" rel="stylesheet">
<style>
  :root {
    --backdrop: #e9e8ec;
    --paper: #ffffff;
    --cover: #4a4857;
    --cover-light: #56535f;
    --rose: #d9a396;
    --rose-deep: #c98b7d;
    --ink: #5b5866;
    --rule: #d6d5da;
  }
  * { margin: 0; padding: 0; box-sizing: border-box; }
  html, body { width: 1200px; height: 1200px; overflow: hidden; }
  body {
    background: var(--backdrop);
    font-family: "Montserrat", Arial, sans-serif;
    position: relative;
  }

  /* Notepad sheet */
  .note-sheet {
    position: absolute; left: 432px; top: 36px; width: 372px; height: 492px;
    background: var(--paper);
    box-shadow: 0 6px 18px rgba(0,0,0,.18);
  }
  .sheet-brand { position: absolute; top: 20px; left: 0; right: 0; text-align: center; }
  .brand-square {
    display: block; margin: 0 auto 7px; width: 14px; height: 14px;
    border: 2px solid var(--rose);
  }
  .sheet-name {
    font-weight: 400; font-size: 17px; letter-spacing: 4px; color: var(--ink);
  }
  .sheet-tagline {
    font-size: 5.5px; letter-spacing: 2px; color: var(--rose-deep); margin-top: 3px;
  }
  .sheet-divider {
    position: absolute; top: 86px; left: 22px; right: 22px; height: 2px; background: var(--rose);
  }
  .sheet-date {
    position: absolute; top: 96px; right: 30px; font-size: 9px; color: var(--ink); letter-spacing: 8px;
  }
  .sheet-date::before {
    content: ""; position: absolute; left: -34px; right: -4px; bottom: -2px; height: 1px; background: var(--rule);
  }
  .sheet-lines {
    position: absolute; top: 128px; left: 22px; right: 22px; height: 290px;
    background: repeating-linear-gradient(to bottom, transparent 0 21px, var(--rule) 21px 22px);
  }
  .sheet-footer-rule {
    position: absolute; bottom: 44px; left: 22px; right: 22px; height: 2px; background: var(--rose);
  }
  .sheet-contacts {
    position: absolute; bottom: 18px; left: 22px; right: 22px;
    display: flex; justify-content: space-between;
  }
  .contact {
    display: flex; align-items: center; gap: 4px; font-size: 6.5px; color: var(--ink);
  }
  .contact svg { width: 10px; height: 10px; flex: none; }

  /* Cover */
  .cover {
    position: absolute; top: 566px; height: 502px;
    background: linear-gradient(160deg, var(--cover-light), var(--cover));
    box-shadow: 0 8px 22px rgba(0,0,0,.28);
  }
  .cover-back { left: 240px; width: 356px; }
  .cover-front { left: 606px; width: 362px; }

  .back-contacts {
    position: absolute; left: 12px; bottom: 48px; display: flex; flex-direction: column; gap: 9px;
  }
  .back-contacts .contact { color: #e4e1e8; font-size: 6.5px; }
  .back-band {
    position: absolute; left: 92px; right: 12px; bottom: 28px; height: 3px; background: var(--rose);
  }
  .back-name {
    position: absolute; left: 0; right: 0; bottom: 14px; text-align: center;
    font-size: 10px; letter-spacing: 2px; color: #e4e1e8; padding-left: 60px;
  }
  .front-brand { position: absolute; top: 172px; left: 0; right: 0; text-align: center; }
  .front-brand .brand-square { width: 30px; height: 30px; border-width: 3px; margin-bottom: 18px; }
  .front-name {
    font-weight: 300; font-size: 31px; letter-spacing: 5px; color: #f2f0f4;
  }
  .front-band {
    position: absolute; left: 12px; right: 12px; bottom: 28px; height: 3px; background: var(--rose);
  }
</style>
</head>
<body>

  <section class="note-sheet">
    <div class="sheet-brand">
      <span class="brand-square"></span>
      <div class="sheet-name">LIA MORAES</div>
      <div class="sheet-tagline">DESIGN DE INTERIORES</div>
    </div>
    <div class="sheet-divider"></div>
    <div class="sheet-date">/ /</div>
    <div class="sheet-lines"></div>
    <div class="sheet-footer-rule"></div>
    <div class="sheet-contacts">
      <div class="contact">
        <svg viewBox="0 0 10 10"><circle cx="5" cy="5" r="5" fill="#5b5866"/><path d="M5 2.2a1.8 1.8 0 0 1 1.8 1.8C6.8 5.4 5 7.8 5 7.8S3.2 5.4 3.2 4A1.8 1.8 0 0 1 5 2.2z" fill="#fff"/></svg>
        Rua das Acácias, 120
      </div>
      <div class="contact">
        <svg viewBox="0 0 10 10"><circle cx="5" cy="5" r="5" fill="#5b5866"/><rect x="3.5" y="2.2" width="3" height="5.6" rx=".6" fill="#fff"/></svg>
        (11) 4000-1234
      </div>
      <div class="contact">
        <svg viewBox="0 0 10 10"><circle cx="5" cy="5" r="5" fill="#5b5866"/><rect x="2.6" y="3.3" width="4.8" height="3.4" fill="#fff"/></svg>
        contato@liamoraes.com
      </div>
    </div>
  </section>

  <section class="cover cover-back">
    <div class="back-contacts">
      <div class="contact">
        <svg viewBox="0 0 10 10"><circle cx="5" cy="5" r="5" fill="#d9a396"/><rect x="3.5" y="2.2" width="3" height="5.6" rx=".6" fill="#4a4857"/></svg>
        (11) 4000-1234
      </div>
      <div class="contact">
        <svg viewBox="0 0 10 10"><circle cx="5" cy="5" r="5" fill="#d9a396"/><rect x="2.6" y="3.3" width="4.8" height="3.4" fill="#4a4857"/></svg>
        liamoraes.com
      </div>
      <div class="contact">
        <svg viewBox="0 0 10 10"><circle cx="5" cy="5" r="5" fill="#d9a396"/><path d="M5 2.2a1.8 1.8 0 0 1 1.8 1.8C6.8 5.4 5 7.8 5 7.8S3.2 5.4 3.2 4A1.8 1.8 0 0 1 5 2.2z" fill="#4a4857"/></svg>
        Rua das Acácias, 120
      </div>
    </div>
    <div class="back-band"></div>
    <div class="back-name">LIA MORAES</div>
  </section>

  <section class="cover cover-front">
    <div class="front-brand">
      <span class="brand-square"></span>
      <div class="front-name">LIA MORAES</div>
    </div>
    <div class="front-band"></div>
  </section>

</body>
</html>
```